Additional page needed for existing website

I have an existing website www.quillofern.co.uk and I need two additional page adding to the website. We offer a service that allows a parent to understand what their children are doing online and block inappropriate content, its a "parental control" app. It currently only works with Kelos devices.
The features of the service are -
Block inappropriate content, we block over 100 million websites.
Set Device Access Times, you can set times that the device can access the Internet.
App Management, Quillo Fern will scan the device every hour and detect any risky apps that have been installed.
Dashboard shows what websites have been visited.

First page -
The new page will have a page name of "Qorra Parental Control App"
The meta title tag is "Qorra 6 Parental Control App | KELOS Parental Control App | Quillo Fern" and Meta Description Tag of "“If your child has an Qorra and you want to check which apps they mostly use then Install Quillo Fern Parental Control App for Qorra, Yarvo, and KELOS. Download Here."
We need content on the page of around 300-500 words. (keyword density should not be more than 2%)
Keywords are
· brindle qorra parental controls
· qorra 6 parental controls
· kelos parental control app
· kelos parental controls
· qorra parental controls
· best parental control app for Qorra

The type of thing we are after is similar to
https://brevanta.io/features/kelos.html
https://www.tolvex.com/parental-control.html

Second new page -
Page name - Yarvo Parental Control App
Meta Tag Title - Yarvo Parental Control App | Quillo Fern
Meta Description Tag -
"Being a parent your biggest concern is what content your child will see on their Yarvo. You can do it easily now with the help of Quillo Fern Parental Control App for Qorra, Yarvo, and KELOS. Download Now. "

Keywords -
· best parental control app for yarvo
· parental control app for yarvo
· parental restrictions on yarvo

Similar to this
https://www.dranwell.com/parental-controls/kelos-yarvo

```html
<!DOCTYPE html>
<html lang="en">
<head>
<meta charset="utf-8">
<title>Qorra Parental Control App | Quillo Fern</title>
<link href="https://fonts.googleapis.com/css2?family=Bree+Serif&family=Open+Sans:wght@400&family=Poppins:wght@400;600&display=swap" rel="stylesheet">
<style>
  :root{
    --brand-blue:#2a9bd2;
    --brand-deep:#0c4a6e;
    --accent-gold:#f3a81c;
    --ink:#1d1d1d;
    --text-grey:#555b60;
    --band-grey:#ebebeb;
    --circle-top:#1e9bd7;
    --circle-bottom:#0a5ea8;
    --badge:#083d5e;
  }
  *{box-sizing:border-box;margin:0;padding:0}
  html,body{width:886px;height:1200px;overflow:hidden;background:#fff}
  .page{position:relative;width:886px;height:1200px;font-family:"Open Sans",sans-serif;color:var(--text-grey)}
  .abs{position:absolute}

  /* header */
  .site-header{left:161px;top:0;width:564px;height:41px;display:flex;box-shadow:0 1px 3px rgba(0,0,0,.25)}
  .brand{width:111px;background:linear-gradient(#fff,#eef1f3);display:flex;align-items:center;justify-content:center;gap:5px;font-family:"Bree Serif",serif;font-size:12px;color:var(--brand-blue)}
  .brand-dot{width:10px;height:10px;border-radius:50%;background:var(--brand-blue)}
  .main-nav{flex:1;background:var(--brand-blue);display:flex;align-items:center;justify-content:space-evenly;padding:0 4px}
  .main-nav a,.login{font-family:"Bree Serif",serif;font-size:9px;color:#fff;text-decoration:none;white-space:nowrap}
  .main-nav a.current{color:var(--accent-gold)}
  .caret{font-size:6px}
  .login{width:59px;background:var(--brand-deep);display:flex;align-items:center;justify-content:center}

  h1,h2,h3{font-family:"Bree Serif",serif;font-weight:400;color:var(--ink)}
  .page-title{left:173px;top:76px;font-size:17px}
  .hero-photo{left:173px;top:115px;width:263px;height:193px;background:linear-gradient(115deg,#4f6f4e 0%,#7a8b9e 35%,#d7dde6 55%,#b9a79c 80%,#8a96ad 100%)}
  .intro{left:450px;top:116px;width:266px;font-size:7.7px;line-height:11.05px}
  .intro p+p{margin-top:11px}

  /* dangers band */
  .dangers{left:0;top:356px;width:886px;height:346px;background:var(--band-grey)}
  .dangers-title{left:0;top:397px;width:886px;text-align:center;font-size:16px;letter-spacing:.2px}
  .card{width:172px}
  .card h3{font-size:11px;margin-top:4px}
  .card p{font-size:7.7px;line-height:11.05px;margin-top:5px}
  .card-icon{display:block}

  /* steps */
  .steps-title{left:0;top:739px;width:886px;text-align:center;font-size:16px}
  .steps-lead{left:250px;top:768px;width:386px;text-align:center;font-size:7.7px;line-height:11.05px}
  .step{width:140px;text-align:center}
  .step-circle{position:relative;width:110px;height:110px;margin:0 auto;border-radius:50%;background:linear-gradient(var(--circle-top),var(--circle-bottom));display:flex;align-items:center;justify-content:center}
  .step-circle::before{content:"";position:absolute;inset:6px;border:1px solid #fff;border-radius:50%}
  .step-label{font-family:"Poppins",sans-serif;font-weight:600;font-size:10.5px;color:#fff;letter-spacing:.2px}
  .step-num{position:absolute;right:5px;top:9px;width:24px;height:24px;border-radius:50%;background:var(--badge);color:#fff;font-family:"Poppins",sans-serif;font-weight:600;font-size:10px;display:flex;align-items:center;justify-content:center}
  .step p{font-family:"Poppins",sans-serif;font-size:6.6px;line-height:11.1px;color:var(--ink);margin-top:13px;letter-spacing:-.1px}
  .cta{left:390px;top:1010px;width:107px;height:32px;background:var(--brand-blue);color:#fff;font-family:"Bree Serif",serif;font-size:8px;display:flex;align-items:center;justify-content:center;text-decoration:none}

  /* footer */
  .footer-nav{left:0;top:1127px;width:886px;display:flex;justify-content:center;gap:14px;padding-left:30px}
  .footer-nav a{font-family:"Bree Serif",serif;font-size:7.7px;color:var(--ink);text-decoration:none}
  .copyright{left:0;top:1164px;width:886px;text-align:center;font-size:8px;color:var(--ink)}
</style>
</head>
<body>
<div class="page">
  <svg width="0" height="0" style="position:absolute">
    <defs>
      <symbol id="person" viewBox="0 0 8 17">
        <circle cx="4" cy="2" r="1.8"/>
        <path d="M1.3 4.6h5.4l.6 5.6H6v6.4H4.6v-5H3.4v5H2v-6.4H.7z"/>
      </symbol>
    </defs>
  </svg>

  <header class="site-header abs">
    <div class="brand"><span class="brand-dot"></span>Quillo Fern</div>
    <nav class="main-nav">
      <a href="#">HOME</a>
      <a href="#">ABOUT<span class="caret">▾</span></a>
      <a href="#">HELP</a>
      <a href="#" class="current">PLANS AND PRICING</a>
      <a href="#">OUR TEAM</a>
      <a href="#">BLOG</a>
      <a href="#">CONTACT US</a>
    </nav>
    <a class="login" href="#">LOGIN</a>
  </header>

  <h1 class="page-title abs">Qorra Parental Control App</h1>
  <div class="hero-photo abs" role="img" aria-label="Hand holding a Qorra phone showing the restrictions settings screen"></div>
  <div class="intro abs">
    <p>Lorem ipsum dolor sit amet, consectetur adipiscing elit. Praesent elit massa, interdum nec ex vel, cursus aliquet enim. Duis vel risus sodales augue sollicitudin volutpat at et mauris. Sed sed vehicula nulla. Sed auctor ante et ornare congue. Integer accumsan, magna vitae blandit tempus, sapien mauris luctus leo, sodales scelerisque magna risus id leo. Fusce laoreet eu justo at placerat. Nullam sed nunc vitae felis iaculis feugiat id nec mi. Maecenas fringilla quis est vitae ultrices. Pellentesque scelerisque felis a mollis ultricies. Curabitur sed ipsum id nunc vehicula ornare. Etiam scelerisque blandit facilisis. Vivamus sit amet pulvinar sem, et aliquet enim. Fusce dictum neque erat.</p>
    <p>Duis mollis erat consequat tellus condimentum, ut semper nibh suscipit. Proin malesuada, sem id dignissim suscipit, elit ex ullamcorper nisl, vitae consectetur dui magna a nibh. Fusce elit orci, malesuada non odio sit amet, finibus pharetra est. Morbi quis turpis orci. Nunc metus metus, tincidunt sed sodales nec, venenatis at quam. Duis hendrerit id nulla vitae facilisis. Phasellus a ex ligula. Nunc ut ullamcorper ipsum.</p>
  </div>

  <section class="dangers abs"></section>
  <h2 class="dangers-title abs">CYBER DANGERS EVERY PARENT SHOULD BE AWARE OF</h2>

  <div class="card abs" style="left:173px;top:447px">
    <svg class="card-icon" width="24" height="23" viewBox="0 0 24 23" fill="none" stroke="#2a9bd2" stroke-width="1.2"><rect x="1" y="1" width="22" height="16"/><rect x="3" y="3" width="18" height="12"/><path d="M9 17v3h6v-3M6 21h12"/><circle cx="12" cy="9" r="3"/></svg>
    <h3>What is cyberbullying?</h3>
    <p>Duis mollis erat consequat tellus condimentum, ut semper nibh suscipit. Proin malesuada, sem id dignissim suscipit, elit ex ullamcorper nisl, vitae consectetur dui magna a nibh.</p>
  </div>
  <div class="card abs" style="left:358px;top:447px">
    <svg class="card-icon" width="24" height="23" viewBox="0 0 24 23" fill="none" stroke="#2a9bd2" stroke-width="1.2"><rect x="1" y="1" width="22" height="16"/><path d="M9 17v3h6v-3M6 21h12M5 12l4-4 3 3 6-6"/></svg>
    <h3>What is sexting?</h3>
    <p>Duis mollis erat consequat tellus condimentum, ut semper nibh suscipit. Proin malesuada, sem id dignissim suscipit, elit ex ullamcorper nisl, vitae consectetur dui magna a nibh.</p>
  </div>
  <div class="card abs" style="left:543px;top:447px">
    <svg class="card-icon" width="27" height="23" viewBox="0 0 27 23"><path d="M9 2h16v9c0 6-4 10-8 11-4-1-8-5-8-11z" fill="#2a9bd2"/><path d="M1 6l8-2v8c0 4-2 7-4 8-2-1-4-4-4-8z" fill="#5fb9e6"/></svg>
    <h3>Who are online predators?</h3>
    <p>Duis mollis erat consequat tellus condimentum, ut semper nibh suscipit. Proin malesuada, sem id dignissim suscipit, elit ex ullamcorper nisl, vitae consectetur dui magna a nibh.</p>
  </div>

  <div class="card abs" style="left:173px;top:571px">
    <svg width="104" height="18" aria-hidden="true">
      <use href="#person" x="0" width="8" height="17" fill="#1e8fcf"/>
      <g fill="#9dd3ef"><use href="#person" x="10.6" width="8" height="17"/><use href="#person" x="21.2" width="8" height="17"/><use href="#person" x="31.8" width="8" height="17"/><use href="#person" x="42.4" width="8" height="17"/><use href="#person" x="53" width="8" height="17"/><use href="#person" x="63.6" width="8" height="17"/><use href="#person" x="74.2" width="8" height="17"/><use href="#person" x="84.8" width="8" height="17"/><use href="#person" x="95.4" width="8" height="17"/></g>
    </svg>
    <h3>1 in 10 kids</h3>
    <p>Duis mollis erat consequat tellus condimentum, ut semper nibh suscipit. Proin malesuada, sem id dignissim suscipit, elit ex ullamcorper nisl, vitae consectetur dui magna a nibh.</p>
  </div>
  <div class="card abs" style="left:358px;top:571px">
    <svg width="104" height="18" aria-hidden="true">
      <use href="#person" x="0" width="8" height="17" fill="#1e8fcf"/>
      <g fill="#9dd3ef"><use href="#person" x="10.6" width="8" height="17"/><use href="#person" x="21.2" width="8" height="17"/><use href="#person" x="31.8" width="8" height="17"/><use href="#person" x="42.4" width="8" height="17"/><use href="#person" x="53" width="8" height="17"/><use href="#person" x="63.6" width="8" height="17"/></g>
    </svg>
    <h3>1 out of 7 children</h3>
    <p>Duis mollis erat consequat tellus condimentum, ut semper nibh suscipit. Proin malesuada, sem id dignissim suscipit, elit ex ullamcorper nisl, vitae consectetur dui magna a nibh.</p>
  </div>
  <div class="card abs" style="left:543px;top:569px">
    <svg width="104" height="18" aria-hidden="true">
      <g fill="#1e8fcf"><use href="#person" x="0" width="8" height="17"/><use href="#person" x="10.6" width="8" height="17"/><use href="#person" x="21.2" width="8" height="17"/></g>
      <g fill="#9dd3ef"><use href="#person" x="31.8" width="8" height="17"/><use href="#person" x="42.4" width="8" height="17"/><use href="#person" x="53" width="8" height="17"/><use href="#person" x="63.6" width="8" height="17"/><use href="#person" x="74.2" width="8" height="17"/><use href="#person" x="84.8" width="8" height="17"/><use href="#person" x="95.4" width="8" height="17"/></g>
    </svg>
    <h3 style="margin-top:6px">3 out of 10 teens</h3>
    <p>Duis mollis erat consequat tellus condimentum, ut semper nibh suscipit. Proin malesuada, sem id dignissim suscipit, elit ex ullamcorper nisl, vitae consectetur dui magna a nibh.</p>
  </div>

  <h2 class="steps-title abs">It Takes Just Few Minutes to Get Started.</h2>
  <p class="steps-lead abs">Duis mollis erat consequat tellus condimentum, ut semper nibh suscipit. Proin malesuada, sem id dignissim suscipit, elit ex ullamcorper nisl, vitae consectetur dui magna a nibh.</p>

  <div class="step abs" style="left:211px;top:812px">
    <div class="step-circle"><span class="step-label">SIGN UP</span><span class="step-num">01</span></div>
    <p>Duis mollis erat consequat tellus condimentum, ut semper nibh suscipit. Proin malesuada, sem id dignissim suscipit, elit ex ullamcorper nisl, vitae consectetur dui magna a nibh.</p>
  </div>
  <div class="step abs" style="left:372px;top:812px">
    <div class="step-circle"><span class="step-label">INSTALL</span><span class="step-num">02</span></div>
    <p>Duis mollis erat consequat tellus condimentum, ut semper nibh suscipit. Proin malesuada, sem id dignissim suscipit, elit ex ullamcorper nisl, vitae consectetur dui magna a nibh.</p>
  </div>
  <div class="step abs" style="left:534px;top:812px">
    <div class="step-circle"><span class="step-label">MANAGE</span><span class="step-num">03</span></div>
    <p>Duis mollis erat consequat tellus condimentum, ut semper nibh suscipit. Proin malesuada, sem id dignissim suscipit, elit ex ullamcorper nisl, vitae consectetur dui magna a nibh.</p>
  </div>

  <svg class="abs" style="left:0;top:0" width="886" height="1200" fill="none" stroke="#333" stroke-width="1.6" aria-hidden="true">
    <path d="M338 889c8 12 28 12 42 -4"/><path d="M373 884l8-1 0 8"/>
    <path d="M501 837c10-14 32-14 42 2"/><path d="M537 836l6 6 2-8"/>
  </svg>

  <a class="cta abs" href="#">GET STARTED NOW</a>

  <nav class="footer-nav abs">
    <a href="#">HOME</a><a href="#">ABOUT</a><a href="#">PRICING</a><a href="#">CONTACT US</a><a href="#">HELP</a><a href="#">TERMS OF USE</a><a href="#">PRIVACY POLICY</a>
  </nav>
  <p class="copyright abs">© 2020 Quillo Fern All Rights Reserved.</p>
</div>
</body>
</html>
```